Women Web Portal

We are developing an internet portal with content created by and for women in Latin America.
This portal will contain different categories focused on relevant topics for women who are at the same time mothers, lovers, workers, pet-owners, ...

We are looking for design that are at the same time uncluttered, easy-to-use and obvious, and comfy. Pastel colours, buttons using traditional fonts, large space for pictures, highlighted social elements,...

Our target being the middle-class women, we want a design that feels comfortable, real, a bit trendy and traditional, not a Vestry & Holm design, something women can relate to and feel comfortable enough to come back and participate.

Examples of websites:
www.cookvault.example
dama.portalvix.example
www.cabellorivo.example
www.casserol.example
Updates

Hi dear designers. After viewing some first drafts, I have updated the brief so you might have a better understanding of what we are looking for.

Thanks

Reason: We've been away for a while, unavailable to provide adequate feedback to the designs already sent. So we're extending the deadline in order to give time to everyone to adapt their work according to the feedback we'll be providing today.

Target Market(s)

Women between 25 and 50 years from Latin America. Mainly mothers: basically, we want women to interact with each other and with the content of the site so they create a strong community.

Advertisingly speaking, we want to have users, contents and FMCG brands to live together on this website.

Industry/Entity Type

Internet

Requirements
Must have
• Pastel colours for category tabs. Comfortable look & feel.

The design should include 3 different pages:
- Homepage
- Article page
- User profile

The page will be done in responsive design, so design should be thought to be adapted according to the browser (2 or 3 columns).

Thanks for doing it as a PSD file .

The design should also include:
- 8 category tabs
- Space for 728x90px and 300x600px advertising format.
- A relevant menu bar at the beginning of each page
Nice to have
• News feed/best content/most active comments zone: we need to bring forward content to our users so they'll be attracted to visit more pages of the website.

Small format to register (account).

Slider or any other moving objects.

Any idea that would facilitate and increase user participation
Should not have
• Actual text. please use Lorem Ipsum.

```html
<!DOCTYPE html>
<html lang="en">
<head>
<meta charset="utf-8">
<title>Women Web Portal – Homepage</title>
<link rel="stylesheet" href="https://fonts.googleapis.com/css2?family=Arimo:wght@400;700&family=Noto+Serif:ital,wght@1,400;1,700&family=Nunito:wght@400;700&display=swap">
<style>
:root{
  --peach:#fbc9a6;
  --peach-light:#fde4d2;
  --coral:#ef8a6f;
  --coral-deep:#e7705a;
  --cream:#fbf1de;
  --ink:#333333;
  --text:#555555;
  --muted:#8a8a8a;
  --line:#dcdcdc;
  --white:#ffffff;
  --green:#5cba2c;
  --green-dark:#3f9a17;
  --accent:#e7705a;
  --c-mothers:#e0a317;
  --c-lovers:#e8736a;
  --c-workers:#e69a3a;
  --c-fashion:#3aaa4c;
  --c-pets:#1ea89a;
  --c-beauty:#c46be0;
  --date-pink:#c45dd8;
  --date-teal:#1f8f73;
}
*{box-sizing:border-box;margin:0;padding:0}
html,body{width:864px;height:1200px;overflow:hidden}
body{font-family:Arimo,Arial,sans-serif;color:var(--text);font-size:8.5px;line-height:1.4}
.page{position:relative;width:864px;height:1200px;overflow:hidden;
  background:
   radial-gradient(ellipse 520px 260px at 120px 60px,#fbb98d 0%,rgba(251,185,141,0) 100%),
   radial-gradient(ellipse 420px 220px at 800px 40px,#f59a7e 0%,rgba(245,154,126,0) 100%),
   linear-gradient(180deg,#fcd2b2 0px,#fde3cf 300px,#fdf3ec 420px,#ffffff 560px,#fdf5f0 900px,#fbe7dc 975px);}
.abs{position:absolute}

/* header */
.logo{left:152px;top:12px;font-family:Nunito,sans-serif;font-weight:700;font-size:24px;color:var(--white);letter-spacing:.5px}
.slogan{left:276px;top:22px;font-family:"Noto Serif",serif;font-style:italic;font-size:9px;color:var(--white)}
.top-nav{left:498px;top:16px;width:234px;height:24px;background:var(--white);border-radius:4px;display:flex;justify-content:space-around;align-items:center;font-size:8px;color:var(--ink);box-shadow:0 1px 3px rgba(0,0,0,.12)}
.top-nav .current{color:var(--accent)}
.cat-nav{left:140px;top:55px;width:593px;height:34px;background:linear-gradient(#fff,#f1f1f1);border-radius:4px;box-shadow:0 1px 4px rgba(0,0,0,.12);display:flex;align-items:center;padding-left:22px;font-size:8px;color:var(--ink)}
.cat-nav span{margin-right:27px}
.search{position:absolute;right:12px;top:9px;width:110px;height:16px;border-radius:8px;background:#e4e4e4;box-shadow:inset 0 1px 2px rgba(0,0,0,.15);font-family:"Noto Serif",serif;font-style:italic;color:var(--muted);padding:2px 8px;font-size:8px}
.search svg{position:absolute;right:6px;top:4px}

/* hero */
.hero-photo{left:180px;top:90px;width:282px;height:188px;background:radial-gradient(ellipse at 50% 40%,#e9b79c 0%,#d59479 45%,#a9c28a 85%,#fbd6bb 100%)}
.hero-title{left:481px;top:104px;width:230px;font-weight:700;font-size:20px;line-height:22px;color:var(--white);text-shadow:0 1px 2px rgba(0,0,0,.15)}
.hero-meta{left:481px;top:157px;font-family:"Noto Serif",serif;font-style:italic;font-size:8px;color:var(--white)}
.hero-text{left:481px;top:173px;width:210px;font-size:7.5px;line-height:10.5px;color:var(--white)}
.btn-green{background:linear-gradient(#79cf44,var(--green-dark));color:var(--white);font-size:7.5px;font-weight:700;border-radius:4px;text-align:center}
.hero-btn{left:482px;top:239px;width:58px;height:19px;line-height:19px}
.slider-arrows{left:637px;top:256px;width:86px;height:22px;background:#f2f2f2;border-radius:4px 4px 0 0;display:flex}
.slider-arrows span{flex:1;display:flex;align-items:center;justify-content:center;border-right:1px solid #ddd}

/* categories */
.categories{left:140px;top:278px;width:593px;height:216px;background:var(--white);display:flex;box-shadow:0 1px 3px rgba(0,0,0,.08)}
.cat{position:relative;width:98.8px;border-right:1px solid var(--line)}
.cat:last-child{border-right:0}
.cat-label{height:22px;line-height:22px;text-align:center;background:var(--cream);font-family:"Noto Serif",serif;font-style:italic;font-size:8.5px;color:#6b5a47;border-bottom:1px solid #eadcc4}
.cat-photo{height:82px}
.cat-caption{position:absolute;left:0;top:77px;width:82px;padding:2px 3px;font-size:7.5px;line-height:9px;color:var(--white)}
.cat-meta{padding:6px 3px 0;font-family:"Noto Serif",serif;font-style:italic;font-weight:700;font-size:5.6px;letter-spacing:-.2px;white-space:nowrap;color:var(--ink)}
.cat-text{padding:5px 3px 0;font-size:7.5px;line-height:10px;color:var(--text)}
.read-more{position:absolute;background:linear-gradient(#ececec,#cfcfcf);color:#777;font-size:7.5px;text-align:center;height:19px;line-height:19px}
.cat .read-more{right:0;top:177px;width:55px}

/* recent */
.section-head{top:516px;height:24px;line-height:24px;background:var(--cream);text-align:center;font-family:"Noto Serif",serif;font-style:italic;font-size:8.5px;color:#6b5a47;border-top:1px solid #eadcc4;border-bottom:1px solid #eadcc4}
.divider{left:436px;top:516px;width:1px;height:444px;background:var(--line)}
.post-title{left:154px;width:280px;font-weight:700;font-size:19px;color:var(--ink);text-shadow:0 1px 1px rgba(0,0,0,.15)}
.post-thumb{left:154px;width:96px;height:96px;background:#2f2f2f;border:6px solid #e3e3e3}
.post-date{left:148px;width:77px;height:22px;line-height:22px;text-align:center;color:var(--white);font-weight:700;font-size:9.5px}
.post-text{left:266px;width:152px;font-size:7px;line-height:11.5px;color:var(--text)}
.post-meta{left:140px;width:296px;height:18px;line-height:18px;background:var(--cream);padding-left:12px;font-family:"Noto Serif",serif;font-style:italic;font-size:7px;color:var(--muted)}
.post-meta b{color:var(--ink)}
.post-meta .pink{color:var(--date-pink)}
.post-meta .teal{color:var(--date-teal)}
.post-meta .sep{margin:0 4px}
.post-more{left:382px;width:54px}
.pager{left:281px;top:938px;display:flex;gap:5px}
.pager span{width:22px;height:22px;line-height:22px;text-align:center;border:1px solid #d4d4d4;background:#f5f5f5;color:#666;font-size:9px}
.pager .current{background:var(--coral-deep);border-color:var(--coral-deep);color:var(--white)}

/* videos */
.player{left:454px;top:553px;width:264px;height:176px;background:#111}
.player-view{height:150px;background:radial-gradient(ellipse at 45% 50%,#c44fb8 0%,#7a1e72 45%,#2a0a26 80%,#0b0309 100%)}
.player-bar{position:relative;height:26px;background:#1a1a1a;color:#ccc;font-size:7px}
.video-item{left:454px;width:276px;height:66px}
.video-thumb{position:absolute;left:0;top:0;width:91px;height:60px;background:#2a2a2a;display:flex;align-items:center;justify-content:center}
.video-title{position:absolute;left:100px;top:0;width:120px;font-weight:700;font-size:8.5px;line-height:10px;color:var(--ink)}
.video-by{position:absolute;left:100px;top:22px;font-size:7.5px;color:var(--text)}
.video-text{position:absolute;left:100px;top:34px;width:176px;font-size:7px;line-height:10px;color:var(--text)}

/* footer */
.footer{left:0;top:978px;width:864px;height:192px;background:linear-gradient(180deg,#f09a7e,#f08f74 50%,#ee8068)}
.foot-col{top:988px;width:150px}
.foot-col h4{font-family:"Noto Serif",serif;font-style:italic;font-weight:400;font-size:8.5px;color:var(--white);margin-bottom:26px}
.foot-col ul{list-style:none;font-size:7.5px;line-height:12.5px;color:var(--white)}
.foot-col li{position:relative;padding-left:10px;width:120px}
.foot-col li::before{content:"";position:absolute;left:0;top:5px;width:3px;height:3px;background:var(--white)}
.foot-sep{top:1000px;width:1px;height:150px;background:rgba(255,255,255,.25)}
.sub-input{left:598px;top:1030px;width:126px;height:14px;background:var(--white);font-size:7px;color:var(--accent);padding:2px 4px 0 16px}
.sub-input svg{position:absolute;left:4px;top:3px}
.sub-btn{left:598px;top:1048px;width:56px;height:14px;line-height:14px}
.sub-note{left:598px;top:1066px;width:130px;font-size:6px;line-height:8px;color:var(--white)}
.social{left:598px;top:1090px;display:flex;gap:4px}
.social span{width:16px;height:16px;background:var(--white);opacity:.9;border-radius:2px}
.copyright{left:0;top:1170px;width:864px;height:30px;line-height:30px;background:#e26a55;text-align:center;color:var(--white);font-size:7px}
</style>
</head>
<body>
<div class="page">

  <div class="abs logo">Logo here</div>
  <div class="abs slogan">Company slogan here</div>
  <nav class="abs top-nav"><span class="current">home</span><span>about</span><span>blog</span><span>members</span><span>contact</span></nav>

  <nav class="abs cat-nav">
    <span>Mothers</span><span>Lovers</span><span>Workers</span><span>Fashionistas</span><span>Pet Owners</span><span>Beauty Addicts</span>
    <div class="search">search...
      <svg width="7" height="7" viewBox="0 0 10 10"><circle cx="6" cy="4" r="3" fill="none" stroke="#777" stroke-width="1.4"/><line x1="4" y1="6" x2="1" y2="9" stroke="#777" stroke-width="1.6"/></svg>
    </div>
  </nav>

  <div class="abs hero-photo" role="img" aria-label="Featured photo: mother and daughter hugging"></div>
  <h1 class="abs hero-title">Etiam placerat ipsum porttitor ipsum</h1>
  <div class="abs hero-meta">Posted by Admin on Apr 14, 2010</div>
  <p class="abs hero-text">Phasellus luctus odio nec risus. Cum sociis natoque penatibus et magnis dis parturient montes, nascetur ridiculus mus. Quisque malesuada auctor nisl. Fusce non neque. Donec diam lorem, pharetra non, pulvinar id, luctus vel, urna. Nam suscipit, ipsum vitae tincidunt laoreet...</p>
  <div class="abs btn-green hero-btn">READ MORE</div>
  <div class="abs slider-arrows">
    <span><svg width="8" height="10" viewBox="0 0 8 10"><path d="M6 1 2 5l4 4" fill="none" stroke="#aaa" stroke-width="2"/></svg></span>
    <span><svg width="8" height="10" viewBox="0 0 8 10"><path d="M2 1l4 4-4 4" fill="none" stroke="#aaa" stroke-width="2"/></svg></span>
  </div>

  <section class="abs categories">
    <article class="cat">
      <div class="cat-label">Mothers</div>
      <div class="cat-photo" role="img" aria-label="Photo: mother at home" style="background:linear-gradient(135deg,#c68a2e,#f3e3cf)"></div>
      <div class="cat-caption" style="background:var(--c-mothers)">Cras eu eros id dui port luctus</div>
      <div class="cat-meta">Posted by Admin on Feb 13, 2010</div>
      <p class="cat-text">In dolor odio, faucibus at pellentesque ornare, pretium nec diam. Aliquam erat volutpat. Proin vitae</p>
      <div class="read-more">Read More</div>
    </article>
    <article class="cat">
      <div class="cat-label">Lovers</div>
      <div class="cat-photo" role="img" aria-label="Photo: smiling couple" style="background:linear-gradient(135deg,#7fa35e,#d99c82)"></div>
      <div class="cat-caption" style="background:var(--c-lovers)">Cras eu eros id dui port luctus</div>
      <div class="cat-meta">Posted by Admin on Feb 13, 2010</div>
      <p class="cat-text">In dolor odio, faucibus at pellentesque ornare, pretium nec diam. Aliquam erat volutpat. Proin vitae</p>
      <div class="read-more">Read More</div>
    </article>
    <article class="cat">
      <div class="cat-label">Workers</div>
      <div class="cat-photo" role="img" aria-label="Photo: woman in a hard hat" style="background:linear-gradient(135deg,#9cc3d8,#f0d66a 60%,#e9e9e9)"></div>
      <div class="cat-caption" style="background:var(--c-workers)">Cras eu eros id dui port luctus</div>
      <div class="cat-meta">Posted by Admin on Feb 13, 2010</div>
      <p class="cat-text">In dolor odio, faucibus at pellentesque ornare, pretium nec diam. Aliquam erat volutpat. Proin vitae</p>
      <div class="read-more">Read More</div>
    </article>
    <article class="cat">
      <div class="cat-label">Fashionistas</div>
      <div class="cat-photo" role="img" aria-label="Photo: fashionable woman" style="background:linear-gradient(135deg,#6b3b2a,#d9a08a 60%,#f1e3dc)"></div>
      <div class="cat-caption" style="background:var(--c-fashion)">Cras eu eros id dui port luctus</div>
      <div class="cat-meta">Posted by Admin on Feb 13, 2010</div>
      <p class="cat-text">In dolor odio, faucibus at pellentesque ornare, pretium nec diam. Aliquam erat volutpat. Proin vitae</p>
      <div class="read-more">Read More</div>
    </article>
    <article class="cat">
      <div class="cat-label">Pet Owners</div>
      <div class="cat-photo" role="img" aria-label="Photo: woman with her pet" style="background:linear-gradient(135deg,#7cc0e6,#3e9fcf 60%,#d7eef7)"></div>
      <div class="cat-caption" style="background:var(--c-pets)">Cras eu eros id dui port luctus</div>
      <div class="cat-meta">Posted by Admin on Feb 13, 2010</div>
      <p class="cat-text">In dolor odio, faucibus at pellentesque ornare, pretium nec diam. Aliquam erat volutpat. Proin vitae</p>
      <div class="read-more">Read More</div>
    </article>
    <article class="cat">
      <div class="cat-label">Beauty Addicts</div>
      <div class="cat-photo" role="img" aria-label="Photo: woman with beauty products" style="background:linear-gradient(135deg,#f1ece8,#d8b5a1 60%,#f5f5f5)"></div>
      <div class="cat-caption" style="background:var(--c-beauty)">Cras eu eros id dui port luctus</div>
      <div class="cat-meta">Posted by Admin on Feb 13, 2010</div>
      <p class="cat-text">In dolor odio, faucibus at pellentesque ornare, pretium nec diam. Aliquam erat volutpat. Proin vitae</p>
      <div class="read-more">Read More</div>
    </article>
  </section>

  <div class="abs section-head" style="left:140px;width:296px">Recent Posts</div>
  <div class="abs section-head" style="left:436px;width:297px">Recent Videos</div>
  <div class="abs divider"></div>

  <h2 class="abs post-title" style="top:556px">Sed neque ipsum pulvinar</h2>
  <div class="abs post-thumb" style="top:594px"></div>
  <div class="abs post-date" style="top:606px;background:var(--date-pink)">Apr 14, 2019</div>
  <p class="abs post-text" style="top:592px">Morbi condimentum tempus tincidunt. Sed neque ipsum, pulvinar eu tristique sollicitudin, tincidunt at nisl. Aenean feugiat risus sed lacus aliquam et adipiscing elit sodales. Aenean in erat sed neque convallis convallis at eu metus. In varius lacus quis diam cursus posuere. Pellentesque habitant morbi tristique senectus et netus et malesuada fames ac turpis egestas.</p>
  <div class="abs post-meta" style="top:710px">Posted by <b>Admin</b> in <span class="pink">Some Category</span><span class="sep">|</span><b>30 comments</b></div>
  <div class="abs read-more post-more" style="top:710px">Read More</div>

  <h2 class="abs post-title" style="top:748px">Sed neque ipsum pulvinar</h2>
  <div class="abs post-thumb" style="top:786px"></div>
  <div class="abs post-date" style="top:798px;background:var(--date-teal)">Apr 14, 2019</div>
  <p class="abs post-text" style="top:784px">Morbi condimentum tempus tincidunt. Sed neque ipsum, pulvinar eu tristique sollicitudin, tincidunt at nisl. Aenean feugiat risus sed lacus aliquam et adipiscing elit sodales. Aenean in erat sed neque convallis convallis at eu metus. In varius lacus quis diam cursus posuere. Pellentesque habitant morbi tristique senectus et netus et malesuada fames ac turpis egestas.</p>
  <div class="abs post-meta" style="top:900px">Posted by <b>Admin</b> in <span class="teal">Some Category</span><span class="sep">|</span><b>30 comments</b></div>
  <div class="abs read-more post-more" style="top:900px">Read More</div>

  <div class="abs pager"><span>1</span><span class="current">2</span><span>3</span><span>4</span><span>5</span></div>

  <div class="abs player">
    <div class="player-view" role="img" aria-label="Video frame: soft pink out-of-focus lights"></div>
    <div class="player-bar">
      <svg class="abs" style="left:0;top:0" width="264" height="26" viewBox="0 0 264 26">
        <rect x="0" y="0" width="264" height="4" fill="#444"/>
        <rect x="0" y="0" width="110" height="4" fill="#888"/>
        <circle cx="30" cy="2" r="4" fill="#ddd"/>
        <rect x="8" y="11" width="2.5" height="8" fill="#ddd"/><rect x="12" y="11" width="2.5" height="8" fill="#ddd"/>
        <path d="M26 13h3l4-3v10l-4-3h-3z" fill="#ddd"/>
        <rect x="40" y="14" width="50" height="2" fill="#666"/><rect x="61" y="11" width="2" height="8" fill="#ddd"/>
        <text x="177" y="18" fill="#ccc" font-size="7" font-family="Arimo,sans-serif">0:14 / 3:25</text>
        <rect x="221" y="12" width="8" height="6" fill="#e33"/>
        <path d="M235 12h6v6" fill="none" stroke="#ddd" stroke-width="1.4"/>
        <path d="M248 11v3M248 11h3M258 11h-3M258 11v3M248 19v-3M248 19h3M258 19h-3M258 19v-3" stroke="#ddd" stroke-width="1.4"/>
      </svg>
    </div>
  </div>

  <article class="abs video-item" style="top:744px">
    <div class="video-thumb"><svg width="34" height="34" viewBox="0 0 34 34"><circle cx="17" cy="17" r="14" fill="none" stroke="#777" stroke-width="2.5"/><path d="M13 10l11 7-11 7z" fill="#777"/></svg></div>
    <div class="video-title">Lorem ipsum dolor sit amet, elit, sed doconsectetur</div>
    <div class="video-by">by place name here</div>
    <p class="video-text">eiusmod tempor incididunt ut labore et dolore magna aliqua. Ut enim ad minim veniam, quis</p>
  </article>
  <article class="abs video-item" style="top:818px">
    <div class="video-thumb"><svg width="34" height="34" viewBox="0 0 34 34"><circle cx="17" cy="17" r="14" fill="none" stroke="#777" stroke-width="2.5"/><path d="M13 10l11 7-11 7z" fill="#777"/></svg></div>
    <div class="video-title">Lorem ipsum dolor sit amet, elit, sed doconsectetur</div>
    <div class="video-by">by place name here</div>
    <p class="video-text">eiusmod tempor incididunt ut labore et dolore magna aliqua. Ut enim ad minim veniam, quis</p>
  </article>
  <article class="abs video-item" style="top:893px">
    <div class="video-thumb"><svg width="34" height="34" viewBox="0 0 34 34"><circle cx="17" cy="17" r="14" fill="none" stroke="#777" stroke-width="2.5"/><path d="M13 10l11 7-11 7z" fill="#777"/></svg></div>
    <div class="video-title">Lorem ipsum dolor sit amet, elit, sed doconsectetur</div>
    <div class="video-by">by place name here</div>
    <p class="video-text">eiusmod tempor incididunt ut labore et dolore magna aliqua. Ut enim ad minim veniam, quis</p>
  </article>

  <footer class="abs footer"></footer>
  <div class="abs foot-sep" style="left:282px"></div>
  <div class="abs foot-sep" style="left:438px"></div>
  <div class="abs foot-sep" style="left:590px"></div>

  <div class="abs foot-col" style="left:142px">
    <h4>Popular Posts</h4>
    <ul><li>Sed neque ipsum pulvinar eu tristique</li><li>Cras eu eros id dui porttitor luctus</li><li>Vivamus vitae nibh id quam convallis blandit</li><li>Aenean vulputate fermentum ante rhoncus pulvinar</li><li>Ut sagittis ultrices urna eget erat</li></ul>
  </div>
  <div class="abs foot-col" style="left:298px">
    <h4>Recent posts</h4>
    <ul><li>Sed neque ipsum pulvinar eu tristique</li><li>Cras eu eros id dui porttitor luctus</li><li>Vivamus vitae nibh id quam convallis blandit</li><li>Aenean vulputate fermentum ante rhoncus pulvinar</li><li>Ut sagittis ultrices urna eget erat</li></ul>
  </div>
  <div class="abs foot-col" style="left:454px">
    <h4>Recent Comments</h4>
    <ul><li>Sed neque ipsum pulvinar eu tristique</li><li>Cras eu eros id dui porttitor luctus</li><li>Vivamus vitae nibh id quam convallis blandit</li><li>Aenean vulputate fermentum ante rhoncus pulvinar</li><li>Ut sagittis ultrices urna eget erat</li></ul>
  </div>
  <div class="abs foot-col" style="left:610px"><h4>Subscribe with Us</h4></div>

  <div class="abs sub-input">
    <svg width="9" height="7" viewBox="0 0 9 7"><rect x=".5" y=".5" width="8" height="6" fill="none" stroke="#e7705a"/><path d="M.5.5l4 3 4-3" fill="none" stroke="#e7705a"/></svg>
    Your@Email
  </div>
  <div class="abs btn-green sub-btn">Subscribe</div>
  <p class="abs sub-note">You may automatically receive updates and news by email.</p>
  <div class="abs social"><span></span><span></span><span></span></div>

  <div class="abs copyright">Copyright Company Name 2013 / All Rights Reserved.</div>
</div>
</body>
</html>
```